Real Estate and Property Management Company needs new listings

We need a business card for our company, Corvell Realty & Property Management. We maximize financial returns on residential investment properties. By evaluating the current value and health of a property, we devise a financial plan to rehabilitate the property while earning an income over a period of years for rental properties, or suggest meaningful updates and improvements to ensure maximum payout on sales properties.
We would like to see our business cards with the colors black and metallic burgundy. The final design should communicate management and financial growth.

Target Market(s)

Home Owners of single family, detatched residential homes.

Industry/Entity Type

Business

Contact Information for Business Card

Side 1: Dana Corvell
Broker, Owner
Dana@CorvellHomesite.example
555-274-8061 (Cell)
555-318-4470 (Office)
Please incorporate in the design of side 1 that we have been in business for 40 years, along with communicating sales and management.
Side 2: Marisa Corvell
Property Manager
Marisa@CorvellHomesite.example
555-274-8095 (Cell)
555-318-4470 (Office)
Please incorporate that we are a family owner and operated company on side 2.

Font styles to use
Serif

Requirements
Must have
• Elegant, feminine design of metallic burgundy on black on double sided card.
Nice to have
• I would like to see some consistency of design on the front and back of the card, with perhaps a bold, thick line of burgundy on the right, vertical side. I would also like the black card stock to have some geometrical design or texture.
Should not have
• Any of the colors provided below. I cannot choose burgundy, which is the color for our business. Is this the only color selection available?

```html
<!DOCTYPE html>
<html lang="en">
<head>
<meta charset="utf-8">
<title>Corvell Realty &amp; Property Management – Business Cards</title>
<link rel="stylesheet" href="https://fonts.googleapis.com/css2?family=Fira+Sans:ital,wght@0,400;0,500;0,700;1,400&family=Fira+Sans+Condensed:wght@400;600&display=swap">
<style>
  :root {
    --page-bg: #d9d6d2;
    --card-core: #5c1b1f;
    --card-mid: #3e1014;
    --card-edge: #22080a;
    --ink: #ffffff;
    --ink-soft: #f1ebe9;
    --shadow: rgba(0, 0, 0, 0.35);
  }
  * { box-sizing: border-box; margin: 0; padding: 0; }
  html, body {
    width: 1200px;
    height: 900px;
    overflow: hidden;
    background: var(--page-bg);
  }
  .sheet {
    width: 1200px;
    height: 900px;
    display: flex;
    flex-direction: column;
    align-items: center;
    justify-content: center;
    gap: 40px;
  }
  .card {
    position: relative;
    width: 700px;
    height: 400px;
    border-radius: 4px;
    overflow: hidden;
    box-shadow: 0 10px 24px var(--shadow);
    color: var(--ink);
    font-family: "Fira Sans", sans-serif;
    text-align: center;
  }
  .card-texture {
    position: absolute;
    inset: 0;
    background: radial-gradient(ellipse at 50% 50%, var(--card-core) 0%, var(--card-mid) 60%, var(--card-edge) 100%);
  }
  .card-content {
    position: relative;
    height: 100%;
    display: flex;
    flex-direction: column;
    align-items: center;
    padding-top: 36px;
  }
  .company {
    font-weight: 700;
    font-size: 21px;
    letter-spacing: 1.6px;
    text-transform: uppercase;
  }
  .company .amp { font-weight: 400; }
  .tagline {
    margin-top: 12px;
    font-style: italic;
    font-size: 19px;
    line-height: 1.25;
    letter-spacing: 0.6px;
    color: var(--ink-soft);
  }
  .person-name {
    margin-top: 30px;
    font-weight: 700;
    font-size: 36px;
    letter-spacing: 1.2px;
  }
  .person-role {
    font-size: 20px;
    letter-spacing: 1px;
    color: var(--ink-soft);
  }
  .contact {
    margin-top: 40px;
    font-size: 24px;
    line-height: 1.35;
  }
  .contact-row {
    display: flex;
    align-items: center;
    justify-content: center;
    gap: 30px;
  }
  .contact-item {
    display: inline-flex;
    align-items: center;
    gap: 10px;
  }
  .icon { width: 22px; height: 22px; flex: none; }

  .card--owner .tagline { font-size: 19px; }
  .card--owner .person-name {
    margin-top: 54px;
    font-family: "Fira Sans Condensed", sans-serif;
    font-weight: 600;
    font-size: 42px;
  }
  .card--owner .person-role {
    font-family: "Fira Sans Condensed", sans-serif;
    font-size: 24px;
  }
  .card--owner .contact {
    margin-top: 44px;
    font-family: "Fira Sans Condensed", sans-serif;
    font-size: 30px;
  }
</style>
</head>
<body>
<svg width="0" height="0" style="position:absolute" aria-hidden="true">
  <defs>
    <symbol id="icon-mail" viewBox="0 0 24 24">
      <circle cx="12" cy="12" r="12" fill="#fff"/>
      <rect x="6" y="8" width="12" height="8.5" rx="1" fill="#3e1014"/>
      <path d="M6.5 8.6 L12 13 L17.5 8.6" fill="none" stroke="#fff" stroke-width="1.3"/>
    </symbol>
    <symbol id="icon-mobile" viewBox="0 0 24 24">
      <circle cx="12" cy="12" r="12" fill="#fff"/>
      <rect x="8" y="5.5" width="8" height="13" rx="1.6" fill="#3e1014"/>
      <rect x="9.3" y="7.3" width="5.4" height="8.2" fill="#fff"/>
    </symbol>
    <symbol id="icon-phone" viewBox="0 0 24 24">
      <circle cx="12" cy="12" r="12" fill="#fff"/>
      <path d="M8.2 6.2 L10.3 6 L11.3 9 L9.9 10.2 C10.7 11.9 12 13.2 13.8 14.1 L15 12.7 L18 13.7 L17.8 15.8 C17.6 16.9 16.6 17.6 15.5 17.4 C10.9 16.6 7.4 13.1 6.6 8.5 C6.4 7.4 7.1 6.4 8.2 6.2 Z" fill="#3e1014"/>
    </symbol>
  </defs>
</svg>

<main class="sheet">
  <article class="card card--manager">
    <div class="card-texture" role="img" aria-label="Dark burgundy card stock with a fine perforated dot texture"></div>
    <div class="card-content">
      <h1 class="company">Corvell Realty <span class="amp">&amp;</span> Property Management</h1>
      <p class="tagline">Family owner and<br>operated company</p>
      <h2 class="person-name">Marisa Corvell</h2>
      <p class="person-role">Property Manager</p>
      <div class="contact">
        <div class="contact-row">
          <span class="contact-item"><svg class="icon" aria-hidden="true"><use href="#icon-mail"/></svg>Marisa@CorvellHomesite.example</span>
        </div>
        <div class="contact-row">
          <span class="contact-item"><svg class="icon" aria-hidden="true"><use href="#icon-mobile"/></svg>555-274-8095</span>
          <span class="contact-item"><svg class="icon" aria-hidden="true"><use href="#icon-phone"/></svg>555-318-4470</span>
        </div>
      </div>
    </div>
  </article>

  <article class="card card--owner">
    <div class="card-texture" role="img" aria-label="Dark burgundy card stock with a fine perforated dot texture"></div>
    <div class="card-content">
      <h1 class="company">Corvell Realty <span class="amp">&amp;</span> Property Management</h1>
      <p class="tagline">40 years in business with<br>communicating sales and management</p>
      <h2 class="person-name">Dana Corvell</h2>
      <p class="person-role">Broker, Owner</p>
      <div class="contact">
        <div class="contact-row">
          <span class="contact-item"><svg class="icon" aria-hidden="true"><use href="#icon-mail"/></svg>Dana@CorvellHomesite.example</span>
        </div>
        <div class="contact-row">
          <span class="contact-item"><svg class="icon" aria-hidden="true"><use href="#icon-mobile"/></svg>555-274-8061</span>
          <span class="contact-item"><svg class="icon" aria-hidden="true"><use href="#icon-phone"/></svg>555-318-4470</span>
        </div>
      </div>
    </div>
  </article>
</main>
</body>
</html>
```